Luxury packaging graphic design for a new Hair care elixir

We need a packaging design for a new product for our line extension of hair colouring. We have already a packaging that is very well received (all in pink) including all accesories and transport box (attached files).
For a new product - protein for the hair - we need a different design tapping into luxury segment.

Target Market(s)

This product is mainly for women between 25-65 that are looking forward to improve hair strukture and make hair looks better, nicer, softer, healthier. The product in the packaging could be used up to 2x times.

Industry/Entity Type

Hair And Beauty

Font styles to use
Serif
Sans Serif

Colors

Designer to choose colors to be used in the design.

Requirements
Must have
• The material of the packaging are carton/styropor/and glass (attached a picture of packaging design to be adapted). The components are quite small so the packaging plays a big role to increase the value of what it is inside. The packaging needs to be inline with our actual packaging designs and corporate identity as they may be delivered together so as an assamble it should look nice, beautiful and of high quality.
• The graphic design for the different components to be adapted are:
• - grapich design for outside box
• - graphic design for the inside bottles
• - graphic design for the flyer/instructions inside the box
Nice to have
• It needs to feel that the packaging is Wow! It is going to be delivered per post so there have to be a beautiful opening effect. Eventually to work with colours like black, white and gold would give a nice luxury feeling.
• The actual product inside is a concentrated protein component so it is very small, therefore the packaging should show that even if small it is an elixir for the hair.
Should not have
• a totally diffenet look as our actual designs.

```html
<!DOCTYPE html>
<html lang="en">
<head>
<meta charset="utf-8">
<title>Noa Liv – Gilded Drop packaging</title>
<link rel="stylesheet" href="https://fonts.googleapis.com/css2?family=Mulish:wght@300;400&display=swap">
<style>
  :root {
    --backdrop: #e9c3aa;
    --paper: #ffffff;
    --paper-shade: #ececec;
    --copper: #e08a55;
    --copper-line: #d9875a;
    --gold-a: #c98a3a;
    --gold-b: #f1d487;
    --ink: #1d1d1d;
    --ink-soft: #3a3a3a;
    --tray: #d6d6d4;
    --tray-edge: #b9b9b7;
    --tray-rim: #9c9ab8;
    --bottle-a: #b57c50;
    --bottle-b: #c99268;
    --cap: #cda67f;
  }
  * { box-sizing: border-box; margin: 0; padding: 0; }
  html, body { width: 1200px; height: 825px; overflow: hidden; }
  body { background: var(--backdrop); font-family: "Mulish", sans-serif; position: relative; }

  .box-front {
    position: absolute; left: 118px; top: 216px; width: 466px; height: 464px;
    background: linear-gradient(90deg, var(--paper) 0%, var(--paper) 70%, var(--paper-shade) 100%);
    border: 1px solid #6b5d55;
  }
  .brand-name {
    position: absolute; top: 40px; width: 100%; text-align: center;
    font-family: "Mulish", sans-serif; font-weight: 400;
    font-size: 20px; letter-spacing: 4px; color: var(--copper);
  }
  .brand-tagline {
    position: absolute; top: 71px; width: 100%; text-align: center;
    font-size: 7.5px; letter-spacing: 1.6px; color: var(--ink-soft);
  }
  .gold-band {
    position: absolute; top: 94px; left: 0; width: 100%; height: 4px;
    background: linear-gradient(90deg, var(--gold-a), var(--gold-b));
  }
  .hair-artwork {
    position: absolute; top: 100px; left: 0; width: 100%; height: 232px;
    background: radial-gradient(ellipse 38% 60% at 50% 62%, rgba(224,138,85,0.35), rgba(255,255,255,0) 70%);
  }
  .product-title {
    position: absolute; top: 172px; width: 100%; text-align: center;
    font-weight: 400; font-size: 21px; letter-spacing: 0.5px; color: var(--ink);
  }
  .claim-row {
    position: absolute; left: 0; width: 100%; text-align: center;
    font-size: 7.5px; line-height: 8px; letter-spacing: 0.6px; color: var(--ink-soft);
  }
  .claim-row.de { top: 335px; }
  .claim-row.fr { top: 369px; }
  .claim-row.en { top: 402px; }
  .claim-row.volume { top: 434px; }
  .rule { position: absolute; left: 0; width: 100%; height: 1px; background: var(--copper-line); }
  .rule.r1 { top: 354px; } .rule.r2 { top: 389px; } .rule.r3 { top: 420px; }

  .box-tray {
    position: absolute; left: 598px; top: 216px; width: 460px; height: 462px;
    border: 3px solid var(--tray-rim); background: var(--tray-edge); padding: 10px;
  }
  .tray-floor { width: 100%; height: 100%; background: var(--tray); position: relative; }
  .bottle { position: absolute; left: 0; top: 0; }
  .bottle text { font-family: "Mulish", sans-serif; }
</style>
</head>
<body>
  <section class="box-front">
    <div class="brand-name">NOA LIV</div>
    <div class="brand-tagline">SHINE IN YOUR SHADE</div>
    <div class="gold-band"></div>
    <div class="hair-artwork" role="img" aria-label="Flowing copper hair strands with gold speckles"></div>
    <h1 class="product-title">GILDED DROP</h1>
    <p class="claim-row de">STRAHLENDE FÄRBENDE<br>BEHANDLUNG</p>
    <div class="rule r1"></div>
    <p class="claim-row fr">TRAITEMENT DE<br>COLORATION ÉCLANTE</p>
    <div class="rule r2"></div>
    <p class="claim-row en">RADIANT COLORING<br>TREATMENT</p>
    <div class="rule r3"></div>
    <p class="claim-row volume">1:1 60ML ℮</p>
  </section>

  <section class="box-tray">
    <div class="tray-floor">
      <svg class="bottle" width="434" height="436" viewBox="0 0 434 436" aria-label="Gilded Drop bottle">
        <defs>
          <linearGradient id="bottleBody" x1="0" x2="1">
            <stop offset="0" stop-color="#b57c50"/>
            <stop offset="0.5" stop-color="#c99268"/>
            <stop offset="1" stop-color="#b57c50"/>
          </linearGradient>
          <linearGradient id="labelGold" x1="0" x2="1">
            <stop offset="0" stop-color="#c98a3a"/>
            <stop offset="1" stop-color="#f1d487"/>
          </linearGradient>
        </defs>
        <rect x="192" y="34" width="36" height="44" rx="3" fill="#cda67f"/>
        <path d="M165 78 H255 Q265 78 265 96 V390 Q265 406 249 406 H171 Q155 406 155 390 V96 Q155 78 165 78 Z" fill="url(#bottleBody)"/>
        <text x="210" y="143" text-anchor="middle" font-size="12" letter-spacing="2" fill="#f0a070">NOA LIV</text>
        <text x="210" y="154" text-anchor="middle" font-size="4.5" letter-spacing="1" fill="#7a4a2a">SHINE IN YOUR SHADE</text>
        <rect x="155" y="164" width="110" height="2.5" fill="url(#labelGold)"/>
        <text x="210" y="246" text-anchor="middle" font-size="8.5" fill="#f0a070">Gilded drop</text>
        <text x="210" y="322" text-anchor="middle" font-size="4.5" fill="#3a2416">STRAHLENDE FÄRBENDE</text>
        <text x="210" y="328" text-anchor="middle" font-size="4.5" fill="#3a2416">BEHANDLUNG</text>
        <rect x="159" y="334" width="102" height="0.8" fill="#e08a55"/>
        <text x="210" y="346" text-anchor="middle" font-size="4.5" fill="#3a2416">100 ml</text>
      </svg>
    </div>
  </section>
</body>
</html>
```